General Contractors need a new Crisp updated Card Design

We need a new business card design for our company of 25 years based in Toronto call Holvaster Building Inc. : Our goal is to be the leading commercial contractors in Toronto by providing exceptional value to our clients. We work very hard to deliver professional, quality, service in conjunction with consistent price competitiveness to all of our clients on every single project.

Target Market(s)

Design & Build Clients

Industry/Entity Type

Construction Company

Contact Information for Business Card

Address:
18 North Tamlin Glen Road, Unit 57, Marbrook Vale, ON, K7T 2R9
Office: 905-218-5937

Holvasters Logo
Employee Job Description
Employee Cell Phone #
Employee Email
www.holvaster-example.com

Colors

Designer to choose colors to be used in the design.

Requirements
Must have
• Quote Company Saying:
• "Professional. Quality. Service."
Nice to have
• New Crisp up to date look. simple & fresh ( Not to Busy)
Should not have
• NO BLUE PRINTS ON THE BUSINESS CARDS

```html
<!DOCTYPE html>
<html lang="en">
<head>
<meta charset="utf-8">
<title>Holvaster Building Inc. — Business Card</title>
<link href="https://fonts.googleapis.com/css2?family=Cinzel:wght@700&family=Roboto:wght@400;700&display=swap" rel="stylesheet">
<style>
  :root {
    --stage: #262626;
    --teal-deep: #00665d;
    --teal-panel: #16776d;
    --white: #ffffff;
    --ink: #4a4a4a;
    --teal-ink: #00665d;
  }
  * { box-sizing: border-box; margin: 0; padding: 0; }
  html, body { width: 1152px; height: 1200px; overflow: hidden; background: var(--stage); }
  .canvas { position: relative; width: 1152px; height: 1200px; }

  .card {
    position: absolute;
    width: 520px; height: 520px;
    box-shadow: 0 14px 30px rgba(0,0,0,.45);
  }

  /* Front */
  .card--front { left: 60px; top: 70px; background: var(--teal-deep); padding: 34px; }
  .card--front .panel {
    position: relative;
    width: 100%; height: 100%;
    background: linear-gradient(135deg, #2a8479 0%, var(--teal-panel) 50%, #0e6e64 100%);
    display: flex; flex-direction: column; align-items: center; justify-content: center;
    color: var(--white);
    text-align: center;
  }
  .company-name {
    font-family: "Roboto", sans-serif;
    font-weight: 700;
    line-height: 1.2;
  }
  .card--front .company-name { font-size: 36px; }
  .tagline {
    font-family: "Roboto", sans-serif; font-weight: 700;
    font-size: 15px; letter-spacing: 3.5px; margin-top: 60px;
  }

  /* Back */
  .card--back {
    left: 572px; top: 610px;
    background: var(--white);
    border: 14px solid var(--teal-deep);
    padding: 54px 44px;
    font-family: "Roboto", sans-serif;
    color: var(--ink);
  }
  .person__name {
    font-family: "Cinzel", serif; font-weight: 700;
    font-size: 32px; color: var(--teal-ink); letter-spacing: 1px; line-height: 1.1;
  }
  .person__role { font-size: 17px; margin-top: 6px; }
  .contact { list-style: none; margin-top: 24px; }
  .contact li { display: flex; align-items: center; gap: 12px; font-size: 17px; line-height: 27px; }
  .contact svg { width: 16px; height: 16px; fill: var(--teal-ink); flex: none; }

  .company { position: absolute; right: 44px; bottom: 50px; text-align: right; }
  .company__row { display: flex; align-items: center; justify-content: flex-end; gap: 12px; }
  .company__mark { width: 34px; height: 34px; background: var(--teal-deep); flex: none; }
  .card--back .company-name { font-size: 24px; color: var(--teal-ink); }
  .address { font-size: 15px; line-height: 21px; margin-top: 12px; }
</style>
</head>
<body>
<main class="canvas">

  <section class="card card--front" aria-label="Card front">
    <div class="panel" role="img" aria-label="Teal panel with faint angular facet pattern behind the company name">
      <p class="company-name">Holvaster Building Inc.</p>
      <p class="tagline">PROFESSIONAL. QUALITY. SERVICE.</p>
    </div>
  </section>

  <section class="card card--back" aria-label="Card back">
    <h1 class="person__name">MARCUS DELAINE</h1>
    <p class="person__role">Founder &amp; CEO</p>
    <ul class="contact">
      <li>
        <svg viewBox="0 0 16 16" aria-hidden="true"><path d="M4 0h8a1 1 0 0 1 1 1v14a1 1 0 0 1-1 1H4a1 1 0 0 1-1-1V1a1 1 0 0 1 1-1zm1 2v10h6V2zm3 11a1 1 0 1 0 0 2 1 1 0 0 0 0-2z"/></svg>
        416-555-0142
      </li>
      <li>
        <svg viewBox="0 0 16 16" aria-hidden="true"><path d="M3.6 1 6 4.2 4.6 6a9 9 0 0 0 5.4 5.4L11.8 10 15 12.4 13.4 15C6.8 15 1 9.2 1 2.6z"/></svg>
        905-218-5937
      </li>
      <li>
        <svg viewBox="0 0 16 16" aria-hidden="true"><path d="M1 3h14v10H1zm1.5 1.2v.4L8 8.6l5.5-4v-.4z"/></svg>
        mdelaine@holvaster-example.com
      </li>
      <li>
        <svg viewBox="0 0 16 16" aria-hidden="true"><path d="M8 1a7 7 0 1 0 0 14A7 7 0 0 0 8 1zm0 1.5c.8.8 1.4 2.3 1.6 4.5H6.4C6.6 4.8 7.2 3.3 8 2.5zM2.6 7h2.3c.1-1.7.5-3 1-4A5.5 5.5 0 0 0 2.6 7zm8.5 0h2.3a5.5 5.5 0 0 0-3.3-4c.5 1 .9 2.3 1 4zM2.6 9a5.5 5.5 0 0 0 3.3 4c-.5-1-.9-2.3-1-4zm3.8 0c.2 2.2.8 3.7 1.6 4.5.8-.8 1.4-2.3 1.6-4.5zm4.7 0c-.1 1.7-.5 3-1 4a5.5 5.5 0 0 0 3.3-4z"/></svg>
        www.holvaster-example.com
      </li>
    </ul>

    <div class="company">
      <div class="company__row">
        <span class="company__mark" aria-hidden="true"></span>
        <p class="company-name">Holvaster Building Inc.</p>
      </div>
      <p class="address">18 North Tamlin Glen Road, Unit 57<br>Marbrook Vale, ON, K7T 2R9</p>
    </div>
  </section>

</main>
</body>
</html>
```